Information Security Company Business Cards

Using our included logo, we need a business card design. It should have standard contact information such as :

Ravi Tanner
Senior Security Engineer
ravi.tanner@quorvex-hub.com
877.640.3958

Maybe include the website "www.quorvex-hub.com" that we will be redesigning soon.??

open to suggestions of course...

Target Market(s)

Our customers are small to large companies. Generally health-care, financial, insurance and the like.

Industry/Entity Type

Business

Font styles to use
Other font styles liked:
• Something that works with the logo

Requirements
Must have
• Colors should flow with the logo if possible. Or at least we think it should.

```html
<!DOCTYPE html>
<html lang="en">
<head>
<meta charset="utf-8">
<title>Quorvex Hub Business Card</title>
<link rel="stylesheet" href="https://fonts.googleapis.com/css2?family=Montserrat:wght@500;800&family=Open+Sans:wght@400&display=swap">
<style>
  :root {
    --page-bg: #e6e6e8;
    --card-white: #ffffff;
    --brand-blue: #35399b;
    --brand-dark: #333335;
    --text-light: #ffffff;
  }
  html, body {
    margin: 0;
    padding: 0;
    width: 1200px;
    height: 720px;
    overflow: hidden;
    background: var(--page-bg);
  }
  .card {
    position: absolute;
    left: 100px;
    top: 75px;
    width: 1000px;
    height: 570px;
    background: var(--card-white);
    box-shadow: 0 10px 30px rgba(0,0,0,0.18);
    overflow: hidden;
  }
  .card-shapes {
    position: absolute;
    inset: 0;
  }
  .band-blue { fill: var(--brand-blue); }
  .band-dark { fill: var(--brand-dark); }

  .contact-list {
    position: absolute;
    left: 34px;
    top: 298px;
    margin: 0;
    padding: 0;
    list-style: none;
    font-family: "Open Sans", sans-serif;
    font-size: 20px;
    line-height: 32px;
    color: var(--text-light);
    white-space: nowrap;
  }
  .contact-list li {
    display: flex;
    align-items: center;
    gap: 12px;
  }
  .contact-icon {
    width: 18px;
    height: 18px;
    flex: none;
    fill: none;
    stroke: var(--text-light);
    stroke-width: 1.6;
  }

  .identity {
    position: absolute;
    right: 30px;
    top: 30px;
    text-align: right;
    font-family: "Montserrat", sans-serif;
    color: var(--text-light);
    font-variant: small-caps;
    letter-spacing: 1.5px;
    white-space: nowrap;
  }
  .identity-name {
    margin: 0;
    font-size: 38px;
    font-weight: 500;
    line-height: 1.1;
  }
  .identity-title {
    margin: 6px 0 0;
    font-size: 20px;
    font-weight: 500;
  }

  .brand {
    position: absolute;
    left: 490px;
    top: 215px;
    display: flex;
    align-items: center;
    gap: 22px;
  }
  .brand-dot {
    width: 90px;
    height: 90px;
    border-radius: 50%;
    border: 10px solid var(--brand-blue);
    box-sizing: border-box;
    flex: none;
  }
  .brand-name {
    margin: 0;
    font-family: "Montserrat", sans-serif;
    font-weight: 800;
    font-size: 50px;
    line-height: 0.95;
    letter-spacing: 3px;
    color: var(--brand-blue);
    text-transform: uppercase;
    white-space: nowrap;
  }
</style>
</head>
<body>
  <main class="card">
    <svg class="card-shapes" width="1000" height="570" viewBox="0 0 1000 570" aria-hidden="true">
      <polygon class="band-dark" points="620,0 1000,0 1000,160 680,160 620,100"/>
      <polygon class="band-blue" points="0,270 400,270 450,330 450,460 1000,460 1000,570 0,570"/>
    </svg>

    <div class="identity">
      <p class="identity-name">Ravi Tanner</p>
      <p class="identity-title">Senior Security Engineer</p>
    </div>

    <div class="brand">
      <div class="brand-dot"></div>
      <p class="brand-name">Quorvex<br>Hub</p>
    </div>

    <ul class="contact-list">
      <li>
        <svg class="contact-icon" viewBox="0 0 18 18"><rect x="5" y="1.5" width="8" height="15" rx="1.5"/><line x1="8" y1="13.5" x2="10" y2="13.5"/></svg>
        877.640.3958
      </li>
      <li>
        <svg class="contact-icon" viewBox="0 0 18 18"><rect x="1.5" y="4" width="15" height="10"/><polyline points="1.5,4 9,10 16.5,4"/></svg>
        ravi.tanner@quorvex-hub.com
      </li>
      <li>
        <svg class="contact-icon" viewBox="0 0 18 18"><circle cx="9" cy="9" r="7.5"/><ellipse cx="9" cy="9" rx="3.2" ry="7.5"/><line x1="1.5" y1="9" x2="16.5" y2="9"/></svg>
        www.quorvex-hub.com
      </li>
    </ul>
  </main>
</body>
</html>
```